political campaign lawn sign - Governor's Council in Massachuesetts

We are looking for a political lawn sign. We are running a campaign for Governor's Council in Massachusetts. This sign will be on the lawn of homes and businesses so people driving by will see it. It needs to be simple and bold. The last name is long so maybe it could say vote for Marty and then Kolbeck will be big a bold on the next line??
We need it to say:
Vote for Martin Kolbeck
Governor's Council.

Target Market(s)

local residents

Industry/Entity Type

Politcal Campaign

Font styles to use
Sans Serif
Other font styles liked:
• not sure what font but a modern looking one such as Helvetica, Arial, Sans Seri, sharp sans..

Colors
0054AA
0677BA
7BADD7
CADEEF
E8F1F8
00AB8E
00BBA5
67D7C9
C6EFE9
E9F9F6
FFF300
FFF600
FEFA6F
FFFEC7
FFFEE8

Requirements
Must have
• My name written out with a Capital D and R but lower case for every other letter so its Marty Kolbeck
Nice to have
• modern font , the Colors of the lawn sign should have Blue, Yellow and White something bold that will stand out
Should not have
• any maps of Massachusetts

```html
<!DOCTYPE html>
<html lang="en">
<head>
<meta charset="utf-8">
<title>Vote for Marty Kolbeck – Governor's Council Lawn Sign</title>
<link href="https://fonts.googleapis.com/css2?family=Oswald:wght@300;600;700&family=Montserrat:wght@500&display=swap" rel="stylesheet">
<style>
  :root {
    --campaign-blue: #2e3e8c;
    --campaign-yellow: #f3c92e;
    --sign-white: #ffffff;
    --backdrop: #eeefeb;
  }
  html, body {
    margin: 0;
    padding: 0;
    width: 1200px;
    height: 999px;
    overflow: hidden;
    background: var(--backdrop);
  }
  .lawn-sign {
    position: absolute;
    left: 50px;
    top: 135px;
    width: 1100px;
    height: 728px;
    background: var(--sign-white);
    box-shadow: 0 2px 10px rgba(0,0,0,0.12);
  }
  .lawn-sign svg { display: block; }
  .accent-bar { fill: var(--campaign-yellow); }
  .url-band { fill: var(--campaign-blue); }
  .headline {
    font-family: "Oswald", sans-serif;
    font-weight: 600;
    font-size: 136px;
    fill: var(--campaign-blue);
  }
  .candidate-name {
    font-family: "Oswald", sans-serif;
    font-weight: 700;
    font-size: 190px;
    fill: var(--campaign-blue);
  }
  .office-title {
    font-family: "Oswald", sans-serif;
    font-weight: 300;
    font-size: 104px;
    fill: var(--campaign-blue);
  }
  .campaign-url {
    font-family: "Montserrat", sans-serif;
    font-weight: 500;
    font-size: 84px;
    fill: var(--campaign-yellow);
  }
</style>
</head>
<body>
  <div class="lawn-sign">
    <svg width="1100" height="728" viewBox="0 0 1100 728" xmlns="http://www.w3.org/2000/svg">
      <rect class="accent-bar" x="26" y="52" width="222" height="106"/>
      <rect class="accent-bar" x="836" y="52" width="226" height="106"/>
      <text class="headline" x="550" y="162" text-anchor="middle" textLength="510" lengthAdjust="spacingAndGlyphs">VOTE FOR</text>
      <text class="candidate-name" x="26" y="378" textLength="1032" lengthAdjust="spacingAndGlyphs">Marty Kolbeck</text>
      <text class="office-title" x="139" y="520" textLength="806" lengthAdjust="spacingAndGlyphs">GOVERNER'S COUNCIL</text>
      <rect class="url-band" x="29" y="554" width="1030" height="121"/>
      <text class="campaign-url" x="142" y="644" textLength="795" lengthAdjust="spacingAndGlyphs">voteformarty.net</text>
    </svg>
  </div>
</body>
</html>
```